I need three graphics made that will go on walls in a basketball lockerroom

I need three graphics made that will go on a basketball lockerroom wall. Here are the specifics.
Graphic 1 (Size 115" wide by 52" tall, min 150 DPI)
This should be something that displays the acronym for TOLVAR. The main background color should be the teal color attached. Use logos and the other approved colors as needed.
Standards
Intensity
Effort
Grit
Energy
Love
Graphic 2 (Size 88" wide by 52" tall, min 150 DPI)
This one should be on the Navy Blue background color attached
and impactful way say Attitude and Effort
Graphic 3 (Size 100" wide by 18" tall, min 150 DPI)
This goes along the top of the way and needs to say
(THS logo) Stars Lead the Way (Star logo) Tolvar Basketball (THS logo)
All three of these need to feel like they are of the same style. For Graphic #2 I thought something maybe like the attached basketball except use the S Star in the middle and say attitude and effort using the colors .. but I'm open to other ideas

```html
<!DOCTYPE html>
<html lang="en">
<head>
<meta charset="utf-8">
<title>Tolvar Basketball – Locker Room Wall Graphics</title>
<link rel="stylesheet" href="https://fonts.googleapis.com/css2?family=Alfa+Slab+One&family=Barlow+Condensed:ital,wght@1,800&family=Graduate&family=Oswald:wght@600&display=swap">
<style>
  :root {
    --sheet: #c0bfbb;
    --navy: #1f3358;
    --teal: #4ba3a6;
    --teal-deep: #33747e;
    --mist: #a9b2b3;
    --silver: #c9c9c9;
    --white: #ffffff;
    --ink: #111111;
  }
  * { margin: 0; padding: 0; box-sizing: border-box; }
  html, body { width: 1144px; height: 1200px; overflow: hidden; }
  body { position: relative; background: var(--sheet); font-family: "Oswald", sans-serif; }

  .graphic-number {
    position: absolute;
    font-family: Arial, sans-serif;
    font-size: 30px;
    color: var(--ink);
  }

  .graphic { position: absolute; overflow: hidden; }

  /* Graphic 1 – acronym wall */
  .acronym-wall {
    left: 163px; top: 88px; width: 894px; height: 404px;
    background: radial-gradient(ellipse 300px 260px at 42% 52%, #b6b9b8 0%, #8a9ea2 45%, var(--teal-deep) 100%);
  }
  .ball-art {
    position: absolute; left: 480px; top: 0; width: 414px; height: 404px;
    background: radial-gradient(circle at 58% 48%, var(--navy) 0%, var(--navy) 48%, rgba(31,51,88,0.55) 64%, rgba(51,116,126,0) 80%);
  }
  .acronym-words {
    position: absolute; left: 0; top: 0; width: 100%; height: 100%;
  }
  .value-word, .team-word {
    position: absolute; transform-origin: left bottom; transform: rotate(-11deg);
    color: var(--white); line-height: 1; white-space: nowrap;
  }
  .value-word { font-family: "Oswald", sans-serif; font-weight: 600; font-size: 36px; }
  .team-word {
    font-family: "Graduate", serif; font-size: 96px; letter-spacing: 2px;
    color: var(--teal-deep); -webkit-text-stroke: 3px var(--white); paint-order: stroke fill;
  }

  /* Graphic 2 – attitude and effort */
  .attitude-wall { left: 268px; top: 539px; width: 684px; height: 404px; }
  .attitude-wall svg { display: block; }
  .headline { font-family: "Alfa Slab One", serif; fill: var(--white); stroke: var(--teal); stroke-width: 9px; paint-order: stroke fill; stroke-linejoin: round; }
  .headline-small { font-family: "Alfa Slab One", serif; fill: var(--silver); stroke: var(--teal); stroke-width: 5px; paint-order: stroke fill; stroke-linejoin: round; }
  .crest-name { font-family: "Oswald", sans-serif; font-weight: 600; fill: var(--white); }

  /* Graphic 3 – header banner */
  .header-banner {
    left: 215px; top: 989px; width: 790px; height: 142px;
    background: linear-gradient(90deg, var(--teal-deep) 0%, #2b5a72 45%, var(--navy) 100%);
  }
  .school-initials {
    position: absolute; left: 26px; top: 14px;
    font-family: "Barlow Condensed", sans-serif; font-style: italic; font-weight: 800;
    font-size: 104px; line-height: 1; color: var(--silver);
  }
  .slogan {
    position: absolute; left: 222px; top: 22px;
    font-family: "Barlow Condensed", sans-serif; font-style: italic; font-weight: 800;
    font-size: 48px; line-height: 50px; color: var(--white); letter-spacing: 1px;
  }
  .slogan span { display: block; }
  .slogan span:first-child { padding-left: 10px; }
  .banner-mark {
    position: absolute; display: flex; align-items: center; gap: 8px;
    font-family: "Oswald", sans-serif; font-weight: 600; color: var(--white);
  }
  .banner-mark .dot { border-radius: 50%; border: 2px solid var(--white); }
  .team-mark { left: 490px; top: 52px; font-size: 26px; }
  .team-mark .dot { width: 30px; height: 30px; }
  .partner-mark { left: 636px; top: 44px; font-size: 15px; line-height: 1.15; color: #cfc8b8; }
  .partner-mark .dot { width: 40px; height: 40px; border-color: #cfc8b8; }
</style>
</head>
<body>

  <div class="graphic-number" style="left:52px; top:96px;">1</div>
  <div class="graphic-number" style="left:62px; top:539px;">2</div>
  <div class="graphic-number" style="left:79px; top:990px;">3</div>

  <!-- Graphic 1 -->
  <section class="graphic acronym-wall" aria-label="Tolvar acronym wall graphic">
    <div class="ball-art" role="img" aria-label="Navy basketball with white seams over a paint splatter"></div>
    <div class="acronym-words">
      <span class="value-word" style="left:292px; top:44px;">STANDARDS</span>
      <span class="value-word" style="left:272px; top:92px;">INTENSITY</span>
      <span class="value-word" style="left:256px; top:140px;">EFFORT</span>
      <span class="team-word" style="left:46px; top:228px;">TOLVAR</span>
      <span class="value-word" style="left:262px; top:280px;">GRIT</span>
      <span class="value-word" style="left:278px; top:312px;">ENERGY</span>
      <span class="value-word" style="left:348px; top:342px;">LOVE</span>
    </div>
  </section>

  <!-- Graphic 2 -->
  <section class="graphic attitude-wall" aria-label="Attitude and effort wall graphic">
    <svg width="684" height="404" viewBox="0 0 684 404">
      <defs>
        <linearGradient id="cornerTopLeft" x1="0" y1="0" x2="1" y2="0">
          <stop offset="0" stop-color="#4ba3a6"/>
          <stop offset="0.55" stop-color="#6a8c9b"/>
          <stop offset="1" stop-color="#1f3358"/>
        </linearGradient>
        <linearGradient id="cornerBottomRight" x1="0" y1="0" x2="1" y2="0">
          <stop offset="0.2" stop-color="#1f3358"/>
          <stop offset="0.5" stop-color="#6a8c9b"/>
          <stop offset="1" stop-color="#4ba3a6"/>
        </linearGradient>
      </defs>
      <rect width="684" height="404" fill="#1f3358"/>
      <polygon points="0,0 600,0 0,157" fill="url(#cornerTopLeft)"/>
      <polygon points="684,266 684,404 146,404" fill="url(#cornerBottomRight)"/>
      <polygon points="0,141 543,0 684,0 684,266 146,404 0,404" fill="#1f3358"/>

      <rect x="532" y="10" width="116" height="380" rx="30" fill="#2a4670" role="img" aria-label="White silhouette of a player leaping for a dunk"/>

      <g class="team-crest">
        <circle cx="66" cy="90" r="14" fill="none" stroke="#ffffff" stroke-width="3"/>
        <text class="crest-name" x="88" y="101" font-size="30">TOLVAR</text>
      </g>

      <text class="headline" x="40" y="266" font-size="118" textLength="492" lengthAdjust="spacingAndGlyphs" transform="rotate(-12 40 266)">ATTITUDE</text>
      <text class="headline-small" x="37" y="334" font-size="62" textLength="94" lengthAdjust="spacingAndGlyphs" transform="rotate(-12 37 334)">AND</text>
      <text class="headline" x="150" y="342" font-size="118" textLength="368" lengthAdjust="spacingAndGlyphs" transform="rotate(-12 150 342)">EFFORT</text>
    </svg>
  </section>

  <!-- Graphic 3 -->
  <section class="graphic header-banner" aria-label="Stars lead the way header banner">
    <div class="school-initials">THS</div>
    <div class="slogan"><span>STARS LEAD</span><span>THE WAY</span></div>
    <div class="banner-mark team-mark"><span class="dot"></span>TOLVAR</div>
    <div class="banner-mark partner-mark"><span class="dot"></span><span>ASHGROVE<br>BASKETBALL</span></div>
  </section>

</body>
</html>
```